Dental Practice Website design

Design a new website for Brindle Dental Practice.
Design should be warm, neutral in colour, with some small amount of bright colour if needed but kept to a minimum. Website should look professional, high end. Home page should be easy to navigate and simple for patients to be able to book online.
Logo in files along with some examples of websites that we like. Please ask if any further info needed.
Menu should have:
About
New Patients
Treatments
Fees
Contact Us

Industry/Entity Type

Dentistry

Number of Pages Required

4 page

Font styles to use
Sans Serif

Colors

Designer to choose colors to be used in the design.

Requirements
Must have
• zorvex reviews badge, book online button,
Nice to have
• neutral, relaxing colours
Should not have
• harsh, bright colours!

```html
<!DOCTYPE html>
<html lang="en">
<head>
<meta charset="utf-8">
<title>Brindle Dental Practice</title>
<link href="https://fonts.googleapis.com/css2?family=Open+Sans:wght@300;400;600;700;800&display=swap" rel="stylesheet">
<style>
:root{
  --sand:#f1eeea;
  --white:#ffffff;
  --rose:#bf8a8c;
  --rose-deep:#b07a7e;
  --rose-light:#d4aaa8;
  --sage:#9aa797;
  --sage-dark:#8b9889;
  --ink:#2e2a29;
  --muted:#5d5857;
  --line:#d9d4cf;
  --cocoa:#3b2f2d;
  --icon:#b8b2ad;
}
*{box-sizing:border-box;margin:0;padding:0}
html,body{width:1200px;height:3743px;overflow:hidden;background:var(--white)}
body{font-family:"Open Sans",sans-serif;color:var(--ink)}
.page{position:relative;width:1200px;height:3743px;overflow:hidden}
.abs{position:absolute}
.btn{position:absolute;display:flex;align-items:center;justify-content:center;background:var(--sage);color:var(--white);font-size:13px;border-radius:4px;letter-spacing:.3px}
.btn-outline{background:transparent;border:1.5px solid var(--white);font-weight:600}

/* top bar */
.topbar{top:0;left:0;width:1200px;height:38px;background:var(--sand);font-size:13px;color:var(--ink)}
.topbar .social{left:138px;top:12px;display:flex;gap:8px}
.dot{width:14px;height:14px;border-radius:50%;background:#d6d0cb}
.topbar .contact{left:665px;top:10px;display:flex;gap:26px;align-items:center}
.topbar .contact span{display:flex;gap:8px;align-items:center}

/* header */
.header{top:38px;left:0;width:1200px;height:79px;background:var(--white)}
.logo{position:absolute;left:97px;top:6px;width:157px;height:111px;background:var(--white);box-shadow:0 2px 6px rgba(0,0,0,.15);z-index:3;display:flex;flex-direction:column;align-items:center;justify-content:center;gap:6px}
.logo .mark{width:22px;height:22px;background:#9b9592}
.logo .name{font-size:17px;font-weight:300;color:#7b7573;text-align:center;line-height:1.15}
.nav{position:absolute;left:420px;top:31px;display:flex;gap:36px;font-size:13px;color:var(--ink);letter-spacing:.2px}
.search{position:absolute;left:925px;top:30px}
.book{left:972px;top:20px;width:128px;height:38px}

/* hero */
.hero{top:117px;left:0;width:1200px;height:515px;background:linear-gradient(90deg,var(--rose) 0%,var(--rose-deep) 100%)}
.hero-photo{left:60px;top:0;width:640px;height:515px;
  background:
    radial-gradient(ellipse 34% 40% at 50% 42%,rgba(238,205,190,.85),rgba(238,205,190,0) 100%),
    radial-gradient(ellipse 50% 62% at 50% 45%,rgba(122,78,64,.55),rgba(122,78,64,0) 100%),
    radial-gradient(ellipse 40% 22% at 50% 100%,rgba(236,196,198,.7),rgba(236,196,198,0) 100%)}
.hero h1{left:696px;top:62px;color:var(--white);font-size:68px;font-weight:700;line-height:77px}
.hero h2{left:696px;top:226px;color:var(--white);font-size:20px;font-weight:700}
.hero p{left:696px;top:259px;color:var(--white);font-size:12px;width:340px;line-height:17px}
.hero .btn{left:696px;top:313px;width:126px;height:41px}
.dots{left:696px;top:396px;display:flex;gap:8px}
.dots i{display:block;width:12px;height:2px;background:rgba(255,255,255,.5)}
.dots i:first-child{width:22px;background:var(--white)}

/* features */
.features{top:632px;left:0;width:1200px;height:115px;background:var(--sand)}
.feature{position:absolute;top:24px;display:flex;gap:14px;align-items:center}
.feature b{display:block;font-weight:300;font-size:30px;line-height:32px;color:var(--ink)}
.feature small{display:block;font-size:15px;color:var(--muted)}

/* split sections */
.label{font-size:14px;color:var(--ink);text-transform:uppercase}
.heading{font-size:31px;font-weight:600;color:var(--ink);line-height:38px}
.body{font-size:11.5px;line-height:17px;color:var(--muted)}
.about-photo{left:587px;top:747px;width:613px;height:558px;
  background:
    radial-gradient(ellipse 30% 22% at 52% 62%,rgba(246,238,232,.95),rgba(246,238,232,0) 100%),
    radial-gradient(ellipse 38% 30% at 48% 32%,rgba(226,186,168,.9),rgba(226,186,168,0) 100%),
    radial-gradient(ellipse 70% 60% at 50% 50%,#b89585,#6f5a52 70%,#3c302c)}
.join-photo{left:0;top:1305px;width:588px;height:556px;
  background:
    radial-gradient(ellipse 14% 10% at 45% 20%,rgba(84,112,150,.7),rgba(84,112,150,0) 100%),
    radial-gradient(ellipse 22% 40% at 22% 62%,rgba(250,250,250,.9),rgba(250,250,250,0) 100%),
    radial-gradient(ellipse 22% 40% at 80% 60%,rgba(250,250,250,.9),rgba(250,250,250,0) 100%),
    radial-gradient(ellipse 18% 20% at 62% 90%,rgba(140,150,170,.7),rgba(140,150,170,0) 100%),
    linear-gradient(135deg,#b3aea8,#e9e6e1 45%,#c5c2bd)}

/* caring */
.caring{top:1861px;left:0;width:1200px;height:417px;background:linear-gradient(90deg,#978a8c,#8c9b97 55%,#a2b39c)}
.compare{left:628px;top:73px;width:481px;height:270px;border-radius:6px;overflow:hidden}
.compare .before{position:absolute;left:0;top:0;width:242px;height:270px;
  background:radial-gradient(ellipse 60% 22% at 55% 50%,#e2d6c6,rgba(226,214,198,0) 100%),radial-gradient(ellipse 80% 55% at 50% 50%,#9a5255,#c89a94 80%)}
.compare .after{position:absolute;left:242px;top:0;width:239px;height:270px;
  background:radial-gradient(ellipse 62% 22% at 45% 50%,#f6f2ec,rgba(246,242,236,0) 100%),radial-gradient(ellipse 80% 55% at 50% 50%,#a9585b,#d2a49f 80%)}
.compare .divider{position:absolute;left:241px;top:0;width:2px;height:270px;background:var(--white)}
.compare .knob{position:absolute;left:224px;top:117px;width:36px;height:36px;border-radius:50%;border:2px solid var(--white)}
.compare span{position:absolute;bottom:22px;color:var(--white);font-size:13px;font-weight:600}

/* team */
.center{left:0;width:1200px;text-align:center}
.card{position:absolute;top:2618px;width:230px}
.card .photo{height:204px;
  background:
    radial-gradient(ellipse 22% 24% at 50% 36%,rgba(214,178,156,.9),rgba(214,178,156,0) 100%),
    radial-gradient(ellipse 46% 36% at 50% 100%,rgba(255,255,255,.95),rgba(255,255,255,0) 100%),
    linear-gradient(180deg,#e6e8e9,#cfd4d7)}
.card h4{margin-top:20px;font-size:15px;font-weight:600;color:var(--ink)}
.card p{font-size:12px;color:var(--muted);margin-top:2px}

/* contact */
.contact-sec{top:3019px;left:0;width:1200px;height:398px;
  background:
    radial-gradient(ellipse 30% 40% at 60% 55%,rgba(92,70,64,.8),rgba(92,70,64,0) 100%),
    radial-gradient(ellipse at 55% 60%,#46383a,#2f2624 75%)}
.field{position:absolute;border:1.5px solid #8d8280;border-radius:4px;color:#d8d2ce;font-size:12px;padding:11px 17px}

/* footer */
.footer h5{font-size:13px;font-weight:600;color:var(--ink)}
.footer ul{list-style:none;margin-top:12px}
.footer li{font-size:12px;color:var(--muted);height:22px}
.map{left:706px;top:3466px;width:395px;height:178px;border-radius:4px;
  background:
    radial-gradient(ellipse 30% 30% at 75% 60%,rgba(190,214,170,.8),rgba(190,214,170,0) 100%),
    radial-gradient(ellipse 30% 22% at 25% 80%,rgba(170,200,224,.9),rgba(170,200,224,0) 100%),
    linear-gradient(135deg,#ede7d3,#e2ddc9 50%,#d8dfe2)}
</style>
</head>
<body>
<div class="page">

  <div class="abs topbar">
    <div class="abs social"><i class="dot"></i><i class="dot"></i><i class="dot"></i></div>
    <div class="abs contact">
      <span><svg width="14" height="14" viewBox="0 0 24 24"><path d="M6.6 10.8a15 15 0 006.6 6.6l2.2-2.2c.3-.3.7-.4 1-.2 1.1.4 2.3.6 3.6.6.6 0 1 .4 1 1V20c0 .6-.4 1-1 1A17 17 0 013 4c0-.6.4-1 1-1h3.5c.6 0 1 .4 1 1 0 1.3.2 2.5.6 3.6.1.3 0 .7-.2 1z" fill="#b8b2ad"/></svg>0155 019 3204</span>
      <span><svg width="16" height="12" viewBox="0 0 16 12"><rect width="16" height="12" rx="1" fill="#cfc9c4"/><path d="M0 0l8 6 8-6" stroke="#fff" fill="none"/></svg>hello@brindledental.co</span>
      <span style="font-size:11px">- &nbsp;A&nbsp; +</span>
      <span>English <svg width="10" height="6" viewBox="0 0 10 6"><path d="M1 1l4 4 4-4" stroke="#2e2a29" fill="none"/></svg></span>
    </div>
  </div>

  <div class="abs header">
    <div class="logo"><div class="mark"></div><div class="name">BRINDLE<br>DENTAL PRACTICE</div></div>
    <nav class="nav"><span>ABOUT</span><span>NEW PATIENTS</span><span>TREATMENTS</span><span>FEES</span><span>CONTACT US</span></nav>
    <svg class="search" width="18" height="18" viewBox="0 0 18 18"><circle cx="7.5" cy="7.5" r="6" stroke="#2e2a29" stroke-width="1.5" fill="none"/><path d="M12 12l5 5" stroke="#2e2a29" stroke-width="1.5"/></svg>
    <div class="btn book">BOOK ONLINE</div>
  </div>

  <section class="abs hero">
    <div class="abs hero-photo" role="img" aria-label="Smiling woman with curly hair"></div>
    <h1 class="abs">Your Smile,<br>Our Passion</h1>
    <h2 class="abs">Exceptional Dental Care in Hollowmere</h2>
    <p class="abs">Gentle, Professional, and Personal – Because Your Smile Deserves the Best!</p>
    <div class="btn btn-outline">View More</div>
    <div class="abs dots"><i></i><i></i><i></i><i></i><i></i></div>
  </section>

  <section class="abs features">
    <div class="feature" style="left:102px"><svg width="52" height="64" viewBox="0 0 52 64" fill="none" stroke="#b8b2ad" stroke-width="2"><circle cx="26" cy="16" r="10"/><path d="M4 62V46c0-8 8-14 22-14s22 6 22 14v16z"/><path d="M20 34v12M32 34v12"/></svg><div><b>Meet</b><small>Our Dentists</small></div></div>
    <div class="feature" style="left:356px"><svg width="62" height="64" viewBox="0 0 62 64" fill="none" stroke="#b8b2ad" stroke-width="2"><path d="M4 6l10 30h30l8 10M20 36l-4 26M12 62h26M14 6h22"/></svg><div><b>Our</b><small>Services</small></div></div>
    <div class="feature" style="left:610px"><svg width="64" height="56" viewBox="0 0 64 56" fill="none" stroke="#b8b2ad" stroke-width="2"><circle cx="32" cy="16" r="9"/><circle cx="12" cy="22" r="7"/><circle cx="52" cy="22" r="7"/><path d="M16 54V40c0-7 7-12 16-12s16 5 16 12v14M2 52V42c0-5 4-8 10-8M62 52V42c0-5-4-8-10-8"/></svg><div><b>Connect</b><small>Our Team</small></div></div>
    <div class="feature" style="left:869px"><svg width="64" height="56" viewBox="0 0 64 56" fill="none" stroke="#b8b2ad" stroke-width="2"><path d="M2 36h12v18H2zM14 40h16l10 4 18-8c3 0 4 3 2 5L40 52H14"/><path d="M22 12l2 5h5l-4 3 2 5-5-3-5 3 2-5-4-3h5zM42 6l2 5h5l-4 3 2 5-5-3-5 3 2-5-4-3h5z"/></svg><div><b>4.5</b><small>zorvex Review</small></div></div>
  </section>

  <div class="abs label" style="left:97px;top:894px">About</div>
  <h2 class="abs heading" style="left:97px;top:918px">Brindle Dental Practice</h2>
  <p class="abs body" style="left:97px;top:968px;width:455px">Welcome to our friendly dental practice nestled in the heart of beautiful Hollowmere, UK. Our team of dedicated dentists, hygienists and support staff are here to provide you with exceptional dental care. With a wide array of services, including general and cosmetic dentistry, orthodontics and emergency care, we're confident that we can deliver the highest quality treatment to you and your loved ones.</p>
  <div class="btn" style="left:97px;top:1110px;width:138px;height:38px">EXPLORE MORE</div>
  <div class="abs about-photo" role="img" aria-label="Smiling patient making a heart shape with gloved hands"></div>

  <div class="abs join-photo" role="img" aria-label="Dental team discussing an x-ray in a clinic"></div>
  <div class="abs label" style="left:648px;top:1391px">Join our practice</div>
  <h2 class="abs heading" style="left:648px;top:1414px">If you're looking for<br>an exceptional dental practice</h2>
  <p class="abs body" style="left:648px;top:1504px;width:455px">we're here to help! Our team is made up of highly skilled professionals who are dedicated to ensuring that all our patients receive top-notch care in a welcoming and comfortable environment. Whether you need a routine examination or a more specialised treatment, we have all the resources to provide you with the best dental care possible. Our practice is always up-to-date with the latest techniques and technologies to make sure that our patients receive the best possible results.</p>
  <p class="abs body" style="left:648px;top:1642px;width:455px">We understand that dental care can be expensive which is why we offer affordable prices to ensure that everyone has access to quality care. If you'd like to learn more about our practice, please don't hesitate to contact us.</p>
  <div class="btn" style="left:648px;top:1733px;width:137px;height:38px">JOIN NOW</div>

  <section class="abs caring">
    <h2 class="abs" style="left:97px;top:103px;color:#fff;font-size:31px;font-weight:600">Caring Beyond Smiles</h2>
    <p class="abs" style="left:97px;top:157px;width:460px;color:#fff;font-size:15px;line-height:22px">Your smile is safe in our hands, nurtured with compassion and expertise. We treat every smile as if it were our own, ensuring comfort, care, and confidence in every visit</p>
    <div class="btn btn-outline" style="left:97px;top:263px;width:162px;height:41px">View Smile Gallery</div>
    <div class="abs compare">
      <div class="before" role="img" aria-label="Teeth before treatment"></div>
      <div class="after" role="img" aria-label="Teeth after treatment"></div>
      <div class="divider"></div>
      <div class="knob"></div>
      <span style="left:33px">Before</span><span style="right:30px">After</span>
    </div>
  </section>

  <div class="abs center label" style="top:2361px">Our team</div>
  <h2 class="abs center heading" style="top:2384px;font-size:32px;line-height:38px">We are delighted to introduce you to our experienced<br>and compassionate dental team</h2>
  <p class="abs center body" style="top:2476px;padding:0 215px">Our team comprises highly skilled dental professionals who are dedicated to providing you with high-quality dental care services. Led by our experienced dentist, each member of our team brings their own unique set of skills and expertise.</p>
  <p class="abs center body" style="top:2527px;padding:0 215px">From our friendly reception staff to our knowledgeable hygienists and assistants, our team is here to ensure that you receive personalised dental care that meets your unique needs and preferences. We take great pride in providing a safe, comfortable, and welcoming environment for our patients, and we look forward to serving you with the utmost care and attention.</p>
  <svg class="abs" style="left:64px;top:2720px" width="14" height="28" viewBox="0 0 14 28"><path d="M12 2L2 14l10 12" stroke="#9d9795" stroke-width="2" fill="none"/></svg>
  <svg class="abs" style="left:1120px;top:2720px" width="14" height="28" viewBox="0 0 14 28"><path d="M2 2l10 12L2 26" stroke="#9d9795" stroke-width="2" fill="none"/></svg>
  <div class="card" style="left:98px"><div class="photo" role="img" aria-label="Portrait of a dentist"></div><h4>Members Name</h4><p>Designation/ degree</p></div>
  <div class="card" style="left:354px"><div class="photo" role="img" aria-label="Portrait of a dentist"></div><h4>Members Name</h4><p>Designation/ degree</p></div>
  <div class="card" style="left:614px"><div class="photo" role="img" aria-label="Portrait of a dentist"></div><h4>Members Name</h4><p>Designation/ degree</p></div>
  <div class="card" style="left:872px"><div class="photo" role="img" aria-label="Portrait of a dentist"></div><h4>Members Name</h4><p>Designation/ degree</p></div>
  <div class="btn" style="left:497px;top:2912px;width:205px;height:39px">VIEW ALL TEAM MEMBERS</div>

  <section class="abs contact-sec" role="img" aria-label="Dim background of a smiling face">
    <h2 class="abs center" style="top:53px;color:#fff;font-size:30px;font-weight:600">Get In Touch</h2>
    <div class="field" style="left:102px;top:124px;width:315px;height:39px">Ful Name*</div>
    <div class="field" style="left:443px;top:124px;width:315px;height:39px">Email ID*</div>
    <div class="field" style="left:783px;top:124px;width:315px;height:39px">Phone Number*</div>
    <div class="field" style="left:102px;top:192px;width:996px;height:64px">Mesage</div>
    <div class="btn" style="left:542px;top:299px;width:119px;height:38px">SUBMIT</div>
  </section>

  <footer class="footer">
    <div class="abs" style="left:99px;top:3470px"><h5>Quick Links</h5><ul><li>Lorem Ipsum</li><li>Lorem Ipsum</li><li>Lorem Ipsum</li><li>Lorem Ipsum</li><li>Lorem Ipsum</li><li>Lorem Ipsum</li><li>Lorem Ipsum</li></ul></div>
    <div class="abs" style="left:263px;top:3470px"><h5>Quick Links</h5><ul><li>Lorem Ipsum</li><li>Lorem Ipsum</li><li>Lorem Ipsum</li><li>Lorem Ipsum</li><li>Lorem Ipsum</li><li>Lorem Ipsum</li><li>Lorem Ipsum</li></ul></div>
    <div class="abs" style="left:434px;top:3470px;width:250px">
      <h5>Contact Us</h5>
      <div style="display:flex;gap:14px;margin-top:16px;font-size:16px;color:var(--muted)"><svg width="16" height="16" viewBox="0 0 24 24"><path d="M6.6 10.8a15 15 0 006.6 6.6l2.2-2.2c.3-.3.7-.4 1-.2 1.1.4 2.3.6 3.6.6.6 0 1 .4 1 1V20c0 .6-.4 1-1 1A17 17 0 013 4c0-.6.4-1 1-1h3.5c.6 0 1 .4 1 1 0 1.3.2 2.5.6 3.6.1.3 0 .7-.2 1z" fill="#cfc9c4"/></svg>0155 019 3204</div>
      <div style="display:flex;gap:14px;margin-top:10px;font-size:16px;color:var(--muted)"><svg width="16" height="12" viewBox="0 0 16 12" style="margin-top:5px"><rect width="16" height="12" rx="1" fill="#cfc9c4"/><path d="M0 0l8 6 8-6" stroke="#fff" fill="none"/></svg>hello@brindledental.co</div>
      <div style="display:flex;gap:14px;margin-top:10px;font-size:12px;line-height:17px;color:var(--muted)"><svg width="16" height="20" viewBox="0 0 16 20" style="flex:none"><path d="M8 0a8 8 0 018 8c0 6-8 12-8 12S0 14 0 8a8 8 0 018-8z" fill="#cfc9c4"/><circle cx="8" cy="8" r="3" fill="#fff"/></svg>Lorem ipsum dolor sit amet, consectetur adipiscing elit. In interdum eu leo ut vulputate.</div>
    </div>
    <div class="abs map" role="img" aria-label="Street map showing the practice location"></div>
    <div class="abs" style="left:97px;top:3690px;width:1004px;height:1px;background:var(--line)"></div>
    <div class="abs" style="left:97px;top:3710px;font-size:10px;color:var(--muted)">Copyright © 2025. All Rights Reserved</div>
    <div class="abs" style="left:1036px;top:3709px;display:flex;gap:8px"><i class="dot"></i><i class="dot"></i><i class="dot"></i></div>
  </footer>

</div>
</body>
</html>
```